Graphic Design Project

Hi,

I would like to create a beer label for our new beer we are creating,

We are called "The Marrowfield Brewing Co."

Our new beer is called "The Wandering Lamplighter" which is a "Pale Ale" with an "ABV 4.8%"

our tag line is "Built For Sessionability"

Everything writen in inverted comma's I would like on the label

I would like it to be a round beer label as well with some sort of picture in the background.

This is our first design of any kind for the company so we do not have a logo or any designs so its open to anything. I would like it to be new and trendy with an older style feel to it.

Industry/Entity Type

Graphic Design

Requirements
Must have
• Round so I can convert into a beer coaster,
needs to have alcohol percentage.

```html
<!DOCTYPE html>
<html lang="en">
<head>
<meta charset="utf-8">
<title>The Wandering Lamplighter – Pale Ale Label</title>
<link rel="stylesheet" href="https://fonts.googleapis.com/css2?family=Montserrat:wght@500&family=Playfair+Display:wght@900&display=swap">
<style>
  :root {
    --label-green: #a6d05a;
    --band-black: #000000;
    --malt-cream: #fde7a0;
    --page-white: #ffffff;
  }
  html, body {
    margin: 0;
    padding: 0;
    width: 1200px;
    height: 900px;
    overflow: hidden;
    background: var(--page-white);
  }
  .label {
    display: block;
    width: 1200px;
    height: 900px;
  }
  .label-disc { fill: var(--label-green); }
  .band { fill: var(--band-black); }
  .rim-text {
    font-family: "Montserrat", sans-serif;
    font-weight: 500;
    fill: var(--band-black);
  }
  .rim-text--brewery { font-size: 33px; }
  .rim-text--tagline { font-size: 37px; }
  .beer-name {
    font-family: "Playfair Display", serif;
    font-weight: 900;
    font-size: 46px;
    fill: var(--label-green);
  }
  .beer-style {
    font-family: "Playfair Display", serif;
    font-weight: 900;
    font-size: 150px;
    fill: var(--malt-cream);
  }
  .abv {
    font-family: "Montserrat", sans-serif;
    font-weight: 500;
    font-size: 27px;
    letter-spacing: 2px;
    fill: var(--label-green);
  }
</style>
</head>
<body>
<svg class="label" viewBox="0 0 1200 900" xmlns="http://www.w3.org/2000/svg">
  <defs>
    <clipPath id="disc-clip">
      <circle cx="600" cy="453" r="455"/>
    </clipPath>
    <radialGradient id="grain-field" cx="50%" cy="50%" r="50%">
      <stop offset="0%" stop-color="#d9df86"/>
      <stop offset="70%" stop-color="#c6db78"/>
      <stop offset="100%" stop-color="#a6d05a"/>
    </radialGradient>
    <path id="rim-top" d="M220,453 A380,380 0 1,1 980,453 A380,380 0 1,1 220,453"/>
    <path id="rim-bottom" d="M195,453 A405,405 0 1,0 1005,453 A405,405 0 1,0 195,453"/>
  </defs>

  <circle class="label-disc" cx="600" cy="453" r="455"/>

  <circle class="grain-pattern" cx="600" cy="453" r="360" fill="url(#grain-field)"
          role="img" aria-label="Pattern of scattered wheat ears in pale cream"/>

  <text class="rim-text rim-text--brewery" text-anchor="middle">
    <textPath href="#rim-top" startOffset="481" textLength="800" lengthAdjust="spacing">THE MARROWFIELD BREWING COMPANY</textPath>
  </text>
  <text class="rim-text rim-text--tagline" text-anchor="middle">
    <textPath href="#rim-bottom" startOffset="770" textLength="780" lengthAdjust="spacing">BUILT FOR SESSIONABILITY</textPath>
  </text>

  <g clip-path="url(#disc-clip)">
    <g class="title-band" transform="rotate(-18.5 600 453)">
      <rect class="band" x="-100" y="283" width="1400" height="339"/>
      <text class="beer-name" x="592" y="370" text-anchor="middle"
            textLength="730" lengthAdjust="spacingAndGlyphs">THE WANDERING LAMPLIGHTER</text>
      <text class="beer-style" x="598" y="514" text-anchor="middle"
            textLength="690" lengthAdjust="spacingAndGlyphs">PALE ALE</text>
      <text class="abv" x="598" y="600" text-anchor="middle">ABV 4.8%</text>
    </g>
  </g>
</svg>
</body>
</html>
```